Business Card Design

We need a new business card for our restaurant/motel as we are new owners. Our business is in a small community in a rainforest north of Townsville, Queensland AUSTRALIA and we are on a mountain 3000 feet above sea level. Visitors come here to see the wide variety of birds (This area is especially noted for the cassowary and riflebird), travel the many bush walks and enjoy the cooler climate. We would like you to use as the main colours blue and green - the buildings are painted in those colours and reflect the green for the forest and blue for the rain/sky. Yellow could also be used. The card should be bright and cheerful.
Industry/Entity Type
Travel
Contact Information for Business Card
Ferncliff Lodge Warrabee
Licensed Café/ Restaurant & Motel
14 Tallowood Lane KORRINGA Qld 4829
Ph: 07 4912 3057 Fax: 07 49123094
reception@ferncliffwarrabee.example
www.ferncliffwarrabee.example
like us on linkbook
Look and feel
Each slider illustrates characteristics of the customer's brand and the style your logo design should communicate.

```html
<!DOCTYPE html>
<html lang="en">
<head>
<meta charset="utf-8">
<title>Ferncliff Lodge Warrabee – Business Card</title>
<link rel="stylesheet" href="https://fonts.googleapis.com/css2?family=Questrial&display=swap">
<style>
  :root {
    --backdrop: #2b2b2b;
    --lime: #c6dc3b;
    --leaf: #9cc462;
    --sky-blue: #1b6db4;
    --paper: #ffffff;
  }
  * { margin: 0; padding: 0; box-sizing: border-box; }
  html, body {
    width: 1200px;
    height: 849px;
    overflow: hidden;
    background: var(--backdrop);
  }
  .business-card {
    position: absolute;
    left: 150px;
    top: 146px;
    width: 900px;
    height: 557px;
    background: var(--lime);
    font-family: "Questrial", "Century Gothic", sans-serif;
    color: var(--sky-blue);
    overflow: hidden;
    box-shadow: 0 12px 30px rgba(0, 0, 0, 0.45);
  }
  .brand-panel {
    position: absolute;
    left: 0;
    top: 0;
    width: 255px;
    height: 100%;
    background: var(--paper);
  }
  .brand-mark {
    position: absolute;
    left: 28px;
    top: 70px;
    display: flex;
    align-items: center;
    gap: 12px;
  }
  .brand-mark__dot {
    width: 22px;
    height: 22px;
    border-radius: 50%;
    background: var(--lime);
    flex: none;
  }
  .brand-mark__name {
    font-size: 30px;
    line-height: 1.15;
    color: var(--sky-blue);
  }
  .divider-stripes {
    position: absolute;
    left: 255px;
    top: 0;
    height: 100%;
    display: flex;
  }
  .divider-stripes span { display: block; height: 100%; }
  .stripe-lime  { width: 20px; background: var(--lime); }
  .stripe-gap   { width: 6px;  background: var(--paper); }
  .stripe-leaf  { width: 19px; background: var(--leaf); }
  .stripe-blue  { width: 7px;  background: var(--sky-blue); }
  .business-info {
    position: absolute;
    right: 26px;
    top: 0;
    text-align: right;
  }
  .business-info__name {
    position: absolute;
    right: 0;
    top: 152px;
    font-size: 33px;
    white-space: nowrap;
  }
  .business-info__tagline {
    position: absolute;
    right: 0;
    top: 198px;
    font-size: 21px;
    white-space: nowrap;
  }
  .contact-list {
    position: absolute;
    right: 0;
    top: 340px;
    list-style: none;
    font-size: 24px;
    line-height: 33px;
    white-space: nowrap;
  }
</style>
</head>
<body>
  <article class="business-card">
    <div class="brand-panel">
      <div class="brand-mark">
        <span class="brand-mark__dot"></span>
        <span class="brand-mark__name">Ferncliff<br>Lodge</span>
      </div>
    </div>
    <div class="divider-stripes">
      <span class="stripe-lime"></span>
      <span class="stripe-gap"></span>
      <span class="stripe-leaf"></span>
      <span class="stripe-gap"></span>
      <span class="stripe-blue"></span>
      <span class="stripe-gap"></span>
    </div>
    <div class="business-info">
      <h1 class="business-info__name">Ferncliff Lodge Warrabee</h1>
      <p class="business-info__tagline">Licensed Café/ Restaurant &amp; Motel</p>
      <ul class="contact-list">
        <li>14 Tallowood Lane KORRINGA Qld 4829</li>
        <li>Ph: 07 4912 3057</li>
        <li>Fax: 07 49123094</li>
        <li>reception@ferncliffwarrabee.example</li>
        <li>www.ferncliffwarrabee.example</li>
        <li>like us on linkbook</li>
      </ul>
    </div>
  </article>
</body>
</html>
```